IT Services

We come to you
Only $49/hr
No contract, no monthly fee
Software engineer on staff
remote assistance or visit in your office

On the back of the card I want to list services.

- Server setup
- Network troubleshooting
- Printer setup
- Secure backup setup
- Software installation
- Wireless network setup
- Wired network setup
- Disaster recovery
- Website management
- Any other technology related support
- Email setup
- HIPAA compliance review and setup
Updates

the URL is: BYTEHARBOR.ZONE please use it on the card

On the card we need to mention "Connect remotely to address your IT issues" if there is enough room as well as "we go to you"

Industry/Entity Type

Printer

Contact Information for Business Card

I want a busoiness card to offer my services to doctor offices, it can be dentists, Otamatry, and other professions. I provide the following service. My plan is to go to their office and drop off my card. I don't want them to forget about it that is why I am paying for the design. I like hand writing design formats.

```html
<!DOCTYPE html>
<html lang="en">
<head>
<meta charset="utf-8">
<title>ByteHarbor – Business Card</title>
<link rel="stylesheet" href="https://fonts.googleapis.com/css2?family=Source+Sans+3:wght@400;600;700&display=swap">
<style>
  :root {
    --orange: #f47b20;
    --orange-soft: #f9c49a;
    --navy: #14304f;
    --card: #ffffff;
    --backdrop: #e6e4e1;
  }
  * { margin: 0; padding: 0; box-sizing: border-box; }
  html, body { width: 1200px; height: 1000px; overflow: hidden; }
  body {
    background: var(--backdrop);
    font-family: "Source Sans 3", sans-serif;
    position: relative;
  }
  .card {
    position: absolute;
    left: 265px;
    width: 666px;
    height: 397px;
    background: var(--card);
    box-shadow: 0 2px 8px rgba(0,0,0,0.18);
    overflow: hidden;
  }
  .card--front { top: 73px; }
  .card--back { top: 533px; }

  /* Front */
  .brand-dot {
    position: absolute; left: 62px; top: 50px;
    width: 84px; height: 84px; border-radius: 50%;
    background: var(--orange);
  }
  .brand-name {
    position: absolute; left: 180px; top: 54px;
    font-size: 39px; font-weight: 600; color: var(--navy);
    letter-spacing: -0.3px;
  }
  .brand-url {
    position: absolute; left: 182px; top: 112px;
    font-size: 20px; font-weight: 700; color: var(--navy);
  }
  .offer {
    position: absolute; left: 25px; top: 216px;
    list-style: none; color: var(--orange);
    font-size: 17.5px; line-height: 25.5px;
  }
  .offer__price { font-weight: 700; font-size: 16.5px; }
  .contact {
    position: absolute; right: 25px; top: 224px;
    text-align: right; color: var(--navy);
  }
  .contact__name { font-size: 27px; font-weight: 600; line-height: 36px; letter-spacing: 0.3px; }
  .contact__line {
    font-size: 21px; font-weight: 600; line-height: 28px;
    display: flex; justify-content: flex-end; align-items: center; gap: 3px;
  }
  .contact__line svg { width: 16px; height: 16px; }
  .band { position: absolute; top: 347px; height: 26px; }
  .band--orange { left: 0; width: 398px; background: var(--orange); }
  .band--navy { left: 403px; right: 0; background: var(--navy); }

  /* Back */
  .specialities {
    position: absolute; left: 33px; top: 54px;
  }
  .specialities__title {
    font-size: 20px; font-weight: 600; color: var(--orange);
    line-height: 24px;
  }
  .specialities__list { list-style: none; }
  .specialities__list li {
    display: flex; align-items: center; gap: 5px;
    font-size: 17px; line-height: 22.6px; color: var(--navy);
  }
  .specialities__list svg { width: 16px; height: 14px; flex: none; }
  .promise {
    position: absolute; left: 333px; top: 60px;
    width: 300px; height: 300px; border-radius: 50%;
    border: 14px solid var(--orange-soft);
    display: flex; align-items: center; justify-content: center;
  }
  .promise__text {
    font-size: 19px; font-weight: 700; color: var(--navy);
  }
</style>
</head>
<body>

<section class="card card--front">
  <div class="brand-dot"></div>
  <div class="brand-name">BYTEHARBOR</div>
  <div class="brand-url">www.ByteHarbor.Zone</div>

  <ul class="offer">
    <li class="offer__price">ONLY $49/HR</li>
    <li>NO CONTRACT, NO MONTHLY FEE</li>
    <li>SOFTWARE ENGINEER ON STAFF</li>
    <li>REMOTE ASSISTANCE OR VISIT IN YOUR OFFICE</li>
  </ul>

  <div class="contact">
    <div class="contact__name">DANIEL REYES</div>
    <div class="contact__line">1-800-555-0142
      <svg viewBox="0 0 16 16" aria-hidden="true"><path fill="#14304f" d="M2 5c0-2 2-3 6-3s6 1 6 3v1h-3V5H5v1H2z M4 7h8l2 6H2z"/><circle cx="8" cy="10" r="1.6" fill="#fff"/></svg>
    </div>
    <div class="contact__line">www.ByteHarbor.Zone
      <svg viewBox="0 0 16 16" aria-hidden="true"><circle cx="8" cy="8" r="6.5" fill="none" stroke="#14304f" stroke-width="1.5"/><ellipse cx="8" cy="8" rx="2.8" ry="6.5" fill="none" stroke="#14304f" stroke-width="1.2"/><path d="M1.5 8h13M3 4.5h10M3 11.5h10" stroke="#14304f" stroke-width="1.1"/></svg>
    </div>
  </div>

  <div class="band band--orange"></div>
  <div class="band band--navy"></div>
</section>

<section class="card card--back">
  <div class="specialities">
    <h2 class="specialities__title">SPECIALITIES</h2>
    <ul class="specialities__list">
      <li><svg viewBox="0 0 16 14"><path d="M1.5 7.5l4 4L14.5 2" fill="none" stroke="#f47b20" stroke-width="2"/></svg>Server setup</li>
      <li><svg viewBox="0 0 16 14"><path d="M1.5 7.5l4 4L14.5 2" fill="none" stroke="#f47b20" stroke-width="2"/></svg>Network troubleshooting</li>
      <li><svg viewBox="0 0 16 14"><path d="M1.5 7.5l4 4L14.5 2" fill="none" stroke="#f47b20" stroke-width="2"/></svg>Printer setup</li>
      <li><svg viewBox="0 0 16 14"><path d="M1.5 7.5l4 4L14.5 2" fill="none" stroke="#f47b20" stroke-width="2"/></svg>Secure backup setup</li>
      <li><svg viewBox="0 0 16 14"><path d="M1.5 7.5l4 4L14.5 2" fill="none" stroke="#f47b20" stroke-width="2"/></svg>Software installation</li>
      <li><svg viewBox="0 0 16 14"><path d="M1.5 7.5l4 4L14.5 2" fill="none" stroke="#f47b20" stroke-width="2"/></svg>Wireless network setup</li>
      <li><svg viewBox="0 0 16 14"><path d="M1.5 7.5l4 4L14.5 2" fill="none" stroke="#f47b20" stroke-width="2"/></svg>Wired network setup</li>
      <li><svg viewBox="0 0 16 14"><path d="M1.5 7.5l4 4L14.5 2" fill="none" stroke="#f47b20" stroke-width="2"/></svg>Disaster recovery</li>
      <li><svg viewBox="0 0 16 14"><path d="M1.5 7.5l4 4L14.5 2" fill="none" stroke="#f47b20" stroke-width="2"/></svg>Website management</li>
      <li><svg viewBox="0 0 16 14"><path d="M1.5 7.5l4 4L14.5 2" fill="none" stroke="#f47b20" stroke-width="2"/></svg>Any other technology related support</li>
      <li><svg viewBox="0 0 16 14"><path d="M1.5 7.5l4 4L14.5 2" fill="none" stroke="#f47b20" stroke-width="2"/></svg>Email setup</li>
      <li><svg viewBox="0 0 16 14"><path d="M1.5 7.5l4 4L14.5 2" fill="none" stroke="#f47b20" stroke-width="2"/></svg>HIPAA compliance review and setup</li>
    </ul>
  </div>

  <div class="promise">
    <span class="promise__text">WE COME TO YOU</span>
  </div>
</section>

</body>
</html>
```